Book Cover Design - Rooted Together: 7 Paths to Raise a Household that Blooms

International cover needed for the Australian (Fenwick Marlow/QRT Press 2011) non-fiction book Rooted Together: 7 Paths to Raise a Household that Blooms.

Blurb: With the birth of a baby, come other new beginnings, the birth of a mother, of a father, and of a family. With each stage of a child's growth, and with every new baby, there are more new beginnings. In older cultures and in villages around the world, parenthood was considered a rite of passage but traditions that guided parents into becoming a family have largely been lost - until now.

This ground breaking book walks a new generation of mothers and fathers through the eight steps of the modern parenthood rite of passage, from couple-connection to family-foundations, so they can prepare for and continue to grow a family that thrives.

Bio: Nora Pembridge is a relationship counsellor, parent educator and columnist for Homeward Nursery magazine. She lives in Sydney with her husband, their three gorgeous children and an itinerary of pets. This is her first book.
Updates

Thank you for your patience, I haven't ever done anything like this before and the designs submitted have helped me to be more specific in my requests. Please see the updated brief. The most important point is that I am seeking a TEXT based cover, so BOTH the TITLE and SUBTITLE should take up most of the space, the image could either be in the background with the title and subtitle overlayed, or be much smaller to fit around them. I have attached some more images to the brief, hope they help to convey the 'feel' I am after.  Thanks again!

Reason: Thank you so much for taking an interest in this project, the process has been very educational and helpful for me. While some of the stock art in the submitted designs are great, I've decided to commission a custom illustration which completely captures the meaning of Rooted Together. I will upload the illustration once it's complete for designers who are still interested to use. Thank you for your patience! Nora

Thank you all for your patience and for opening up my thinking about what I am really hoping for with this cover. I have uploaded some new tree designs and more specific instructions that I would like to be included in the cover design. I'm looking forward to seeing your creations!

With warm regards,

Nora

Target Market(s)

Couples thinking about having a baby and new parents of one or more young children.

Industry/Entity Type

Baby

Requirements
Must have
• TEXT based cover with BOTH the TITLE and SUBTITLE taking up most of the page.
Colors to match the Australian version (see attached)
Tree design bottom left (as per Trunk Treatment image attached) OR Heart Tree Design
Root design (as per one of the two images attached)
PLEASE ADD: three new shoots coming up from the ground under the tree to symbolize the children.
Nice to have
• Artistic effect to complement Australian cover.
Subtle retro feel to complement Australian cover.
Should not have
• The book is inclusive of all parents (including same-sex parents) so no images of mother/father and baby.

```html
<!DOCTYPE html>
<html lang="en">
<head>
<meta charset="utf-8">
<title>Rooted Together – Book Cover</title>
<link href="https://fonts.googleapis.com/css2?family=Open+Sans:ital,wght@0,400;1,400&family=Arimo:ital,wght@0,400;1,400&display=swap" rel="stylesheet">
<style>
  :root {
    --page: #ffffff;
    --frame: #111111;
    --band: #046631;
    --title: #ffffff;
    --subtitle: #6b6b6b;
    --author: #111111;
    --sky-top: #b9e2ef;
    --sky-low: #d4eef4;
    --ground: #8a5a1e;
  }
  html, body {
    margin: 0;
    padding: 0;
    width: 1200px;
    height: 1000px;
    overflow: hidden;
    background: var(--page);
  }
  .canvas {
    position: relative;
    width: 1200px;
    height: 1000px;
  }
  .cover {
    position: absolute;
    left: 275px;
    top: 10px;
    width: 650px;
    height: 978px;
    box-sizing: border-box;
    border: 2px solid var(--frame);
    background: var(--page);
  }
  .title-band {
    position: absolute;
    left: 0;
    top: 100px;
    width: 100%;
    height: 262px;
    background: var(--band);
    display: flex;
    align-items: center;
    justify-content: center;
  }
  .title {
    margin: 0;
    text-align: center;
    font-family: "Open Sans", sans-serif;
    font-weight: 400;
    font-size: 122px;
    line-height: 116px;
    color: var(--title);
    letter-spacing: -1px;
  }
  .title span { display: block; white-space: nowrap; }
  .title em { font-style: italic; }
  .subtitle {
    position: absolute;
    right: 66px;
    top: 396px;
    margin: 0;
    text-align: right;
    font-family: "Arimo", sans-serif;
    font-weight: 400;
    color: var(--subtitle);
    white-space: nowrap;
  }
  .subtitle .line { display: block; height: 98px; line-height: 98px; letter-spacing: -2px; }
  .subtitle .line.short { height: 76px; line-height: 76px; letter-spacing: -1px; }
  .big { font-size: 104px; }
  .mid { font-size: 68px; }
  .small { font-size: 48px; }
  .tiny { font-size: 28px; }
  .subtitle em { font-style: italic; }
  .illustration {
    position: absolute;
    right: 66px;
    top: 790px;
    width: 98px;
    height: 108px;
    background: linear-gradient(to bottom, var(--sky-top) 0%, var(--sky-low) 80%, var(--ground) 83%, var(--ground) 100%);
  }
  .author {
    position: absolute;
    left: 0;
    bottom: 30px;
    width: 100%;
    margin: 0;
    text-align: center;
    font-family: "Open Sans", sans-serif;
    font-size: 20px;
    line-height: 28px;
    color: var(--author);
  }
</style>
</head>
<body>
  <div class="canvas">
    <div class="cover">
      <div class="title-band">
        <h1 class="title"><span>Rooted</span><span><em>Together</em></span></h1>
      </div>
      <h2 class="subtitle">
        <span class="line"><span class="big">7Paths</span></span>
        <span class="line"><span class="small">to</span><em class="big">Raise</em></span>
        <span class="line short"><span class="tiny">a</span><span class="mid">Household</span><span class="tiny">that</span></span>
        <span class="line"><em class="big">Blooms</em></span>
      </h2>
      <div class="illustration" role="img" aria-label="Painted illustration of a lone tree on a grassy hill under a pale blue sky"></div>
      <p class="author">NoraPembridge</p>
    </div>
  </div>
</body>
</html>
```